Cardiology practice business card

We need a business card for our cardiology practice "Bellmoor Cardiology". We have a new logo, attached below. We like the colours in the logo - red and charcoal. The front of the business card will need to have the doctors name, address, phone number and email. The back will need to have space to write 2 appointment dates and times.

```html
<!DOCTYPE html>
<html lang="en">
<head>
<meta charset="utf-8">
<title>Bellmoor Cardiology – Business Card</title>
<link href="https://fonts.googleapis.com/css2?family=Archivo:wght@400;600;700&display=swap" rel="stylesheet">
<style>
  :root {
    --backdrop: #f7e6e6;
    --card-front: #ffffff;
    --card-back: #999999;
    --charcoal: #4a4a4a;
    --label: #555555;
    --red: #cc1f24;
    --field: #ffffff;
  }
  * { margin: 0; padding: 0; box-sizing: border-box; }
  html, body {
    width: 1200px;
    height: 800px;
    overflow: hidden;
  }
  body {
    background: var(--backdrop);
    font-family: "Archivo", Arial, sans-serif;
    position: relative;
  }
  .card {
    position: absolute;
    left: 375px;
    width: 450px;
    height: 281px;
  }
  .card--front { top: 88px; background: var(--card-front); }
  .card--back { top: 432px; background: var(--card-back); }

  .brand {
    position: absolute;
    left: 218px;
    top: 46px;
    display: flex;
    align-items: center;
    gap: 10px;
    color: var(--red);
    font-weight: 700;
    font-size: 22px;
    letter-spacing: 0.5px;
    line-height: 1.05;
  }
  .brand__dot {
    width: 14px;
    height: 14px;
    border-radius: 50%;
    background: var(--red);
    flex: none;
  }

  .doctor { position: absolute; left: 44px; top: 146px; }
  .doctor__name {
    font-size: 22px;
    font-weight: 700;
    color: var(--charcoal);
    line-height: 1.1;
  }
  .doctor__role {
    font-size: 13px;
    color: var(--red);
    margin-top: 2px;
  }
  .contact {
    position: absolute;
    left: 44px;
    top: 203px;
    font-size: 13px;
    line-height: 17px;
    color: var(--charcoal);
  }

  .appointment__title {
    position: absolute;
    left: 45px;
    top: 31px;
    font-size: 22px;
    font-weight: 700;
    color: var(--charcoal);
    letter-spacing: 0.3px;
  }
  .slot { position: absolute; }
  .slot__field {
    height: 34px;
    background: var(--field);
  }
  .slot__label {
    font-size: 12px;
    color: var(--label);
    margin-top: 6px;
  }
  .slot--date { left: 45px; width: 222px; }
  .slot--time { left: 284px; width: 122px; }
  .row-1 { top: 79px; }
  .row-2 { top: 146px; }

  .address {
    position: absolute;
    left: 45px;
    top: 224px;
    font-size: 12.5px;
    line-height: 16px;
    color: var(--label);
  }
</style>
</head>
<body>
  <section class="card card--front">
    <div class="brand">
      <span class="brand__dot"></span>
      <span>BELLMOOR<br>CARDIOLOGY</span>
    </div>
    <div class="doctor">
      <p class="doctor__name">Dr. Alan Reeve</p>
      <p class="doctor__role">Cardiologist</p>
    </div>
    <div class="contact">
      <p>+00 00 000 0000</p>
      <p>alan.reeve@bellmoor-cardiology.com</p>
    </div>
  </section>

  <section class="card card--back">
    <h2 class="appointment__title">APPOINTMENT</h2>
    <div class="slot slot--date row-1"><div class="slot__field"></div><p class="slot__label">Date</p></div>
    <div class="slot slot--time row-1"><div class="slot__field"></div><p class="slot__label">Time</p></div>
    <div class="slot slot--date row-2"><div class="slot__field"></div><p class="slot__label">Date</p></div>
    <div class="slot slot--time row-2"><div class="slot__field"></div><p class="slot__label">Time</p></div>
    <address class="address" style="font-style:normal">
      Suite 118 4420 Harlow Crossing,<br>Wenbrook, DE 19820
    </address>
  </section>
</body>
</html>
```